We are looking for a simple design that would be uplifting for
upscale drug addicts

MERIDIAN COLLECTIVE

PLEASE SEE THE LINK FOR TAG LINE AND CONTENT

thank you.

here is all the actual info we need and we want something like this...

http://files.qzr.lumtrabox.example/rest/objects/7c2910e4b557d81a93e40bd59fa644163fe2adf0899f?uid=bdf8e1b9b6f556b6b83c44471fdc79%2fproofs&expires=1482716603&signature=kT9PwLmQxZbVoNHLdtrtlmoGHQB%3d

The shape and colors don't have to be like what I posted it is only an example.

Target Market(s)

Harlow Row, internet and creative types, men, early 30's,
upwardly mobile, drug addicts

current site

brightkestrelway.example

now launching new name Meridian Collective

Industry/Entity Type

Drug

Requirements
Must have
• upscale look, great font
Should not have
• a corporate look but should not look like a clinic.

```html
<!DOCTYPE html>
<html lang="en">
<head>
<meta charset="utf-8">
<title>Meridian Collective — Business Cards</title>
<link rel="stylesheet" href="https://fonts.googleapis.com/css2?family=Archivo+Black&family=Montserrat:wght@700;800&display=swap">
<style>
  :root {
    --backdrop: #e7e4df;
    --ink: #0b0b0b;
    --paper: #ffffff;
    --card-shadow: rgba(0, 0, 0, 0.22);
  }
  * { box-sizing: border-box; margin: 0; padding: 0; }
  html, body {
    width: 1200px;
    height: 800px;
    overflow: hidden;
    background: var(--backdrop);
  }
  .canvas {
    position: relative;
    width: 1200px;
    height: 800px;
  }
  .card {
    position: absolute;
    width: 580px;
    height: 330px;
    border-radius: 16px;
    box-shadow: 0 10px 28px var(--card-shadow);
    --fg: var(--ink);
    background: var(--paper);
    color: var(--fg);
  }
  .card--dark {
    left: 570px;
    top: 55px;
    background: var(--ink);
    --fg: var(--paper);
  }
  .card--light {
    left: 50px;
    top: 415px;
  }
  .emblem-row {
    position: absolute;
    top: 28px;
    left: 0;
    right: 0;
    display: flex;
    justify-content: center;
    align-items: center;
    gap: 22px;
  }
  .emblem-rule {
    width: 84px;
    height: 3px;
    background: var(--fg);
  }
  .emblem-mark {
    width: 30px;
    height: 36px;
    background: var(--fg);
    opacity: 0.85;
    border-radius: 3px;
  }
  .brand-name {
    position: absolute;
    top: 78px;
    left: 0;
    right: 0;
    text-align: center;
    font-family: "Archivo Black", sans-serif;
    font-size: 37px;
    letter-spacing: -0.5px;
    line-height: 1;
  }
  .contact {
    position: absolute;
    top: 142px;
    left: 120px;
    width: 290px;
    padding-top: 10px;
    border-top: 3px solid var(--fg);
    font-family: "Montserrat", sans-serif;
    font-weight: 800;
    line-height: 1.08;
    text-transform: uppercase;
  }
  .contact__name {
    font-family: "Archivo Black", sans-serif;
    font-size: 27px;
    letter-spacing: 2.5px;
    line-height: 1;
  }
  .contact__role,
  .contact__street {
    font-size: 17px;
    letter-spacing: 1.2px;
  }
  .contact__city {
    font-size: 17px;
    letter-spacing: 5px;
  }
  .contact__phone {
    font-size: 19px;
    letter-spacing: 10px;
  }
  .contact__email {
    margin-top: 2px;
    font-size: 10.5px;
    letter-spacing: 0.3px;
  }
</style>
</head>
<body>
<main class="canvas">

  <section class="card card--dark" aria-label="Business card, dark version">
    <div class="emblem-row">
      <span class="emblem-rule"></span>
      <span class="emblem-mark" role="img" aria-label="Small syringe icon"></span>
      <span class="emblem-rule"></span>
    </div>
    <h1 class="brand-name">MERIDIAN COLLECTIVE</h1>
    <address class="contact">
      <div class="contact__name">DANIEL MORVAN</div>
      <div class="contact__role">Program Coordinator</div>
      <div class="contact__street">418 W. 27th St. Suite 302</div>
      <div class="contact__city">New York, NY 10001</div>
      <div class="contact__phone">555.014.2296</div>
      <div class="contact__email">counselor@meridianhealth.example</div>
    </address>
  </section>

  <section class="card card--light" aria-label="Business card, light version">
    <div class="emblem-row">
      <span class="emblem-rule"></span>
      <span class="emblem-mark" role="img" aria-label="Small syringe icon"></span>
      <span class="emblem-rule"></span>
    </div>
    <h2 class="brand-name">MERIDIAN COLLECTIVE</h2>
    <address class="contact">
      <div class="contact__name">DANIEL MORVAN</div>
      <div class="contact__role">Program Coordinator</div>
      <div class="contact__street">418 W. 27th St. Suite 302</div>
      <div class="contact__city">New York, NY 10001</div>
      <div class="contact__phone">555.014.2296</div>
      <div class="contact__email">counselor@meridianhealth.example</div>
    </address>
  </section>

</main>
</body>
</html>
```